Website redesign

We need a bold revamp of our website (http://www.brantwoodpower.co.nz/)
which at the moment looks dated. We want a crisp, fresh and bold look. The background image behind web page can go. Open to complete new layout

Target Market(s)

Electrical contracting company- working in the domestic and commercial field

Coding

Coded - Design and coding required

Number of Pages Required

5+ page

Font styles to use
Sans Serif

Colors

Designer to choose colors to be used in the design.

```html
<!DOCTYPE html>
<html lang="en">
<head>
<meta charset="utf-8">
<title>Brantwood Power – Home</title>
<link href="https://fonts.googleapis.com/css2?family=Arimo:wght@400;700&display=swap" rel="stylesheet">
<style>
  :root {
    --brand-red: #e8130f;
    --ink: #1f2233;
    --navy: #2c3556;
    --muted: #8a93b5;
    --body-text: #6b6f7c;
    --white: #ffffff;
  }
  html, body {
    margin: 0;
    padding: 0;
    width: 1200px;
    height: 676px;
    overflow: hidden;
    background: var(--white);
    font-family: "Arimo", Arial, sans-serif;
  }
  .page {
    position: relative;
    width: 1200px;
    height: 676px;
    overflow: hidden;
    background: var(--white);
  }

  /* Header */
  .site-header {
    position: relative;
    height: 104px;
  }
  .contact-bar {
    position: absolute;
    top: 0;
    left: 0;
    width: 1200px;
    height: 36px;
  }
  .contact-bar__info {
    position: absolute;
    top: 0;
    right: 40px;
    height: 36px;
    display: flex;
    align-items: center;
    gap: 28px;
    color: var(--white);
    font-size: 11px;
    font-weight: 700;
  }
  .contact-bar__item {
    display: flex;
    align-items: center;
    gap: 5px;
  }
  .brand {
    position: absolute;
    left: 40px;
    top: 26px;
    display: flex;
    align-items: center;
    gap: 10px;
  }
  .brand__mark {
    width: 22px;
    height: 22px;
    background: var(--brand-red);
  }
  .brand__name {
    font-size: 30px;
    font-weight: 700;
    color: var(--ink);
    letter-spacing: -0.5px;
  }
  .main-nav {
    position: absolute;
    top: 62px;
    right: 40px;
    display: flex;
    gap: 36px;
    font-size: 13px;
    letter-spacing: 0.3px;
  }
  .main-nav a {
    color: var(--ink);
    text-decoration: none;
  }
  .main-nav a.is-active {
    color: var(--brand-red);
  }

  /* Hero */
  .hero {
    display: block;
    width: 1200px;
    height: 432px;
  }

  /* About */
  .about {
    position: relative;
    height: 140px;
    padding: 0 0 0 90px;
  }
  .about__eyebrow {
    margin: 0;
    padding-top: 18px;
    font-size: 16px;
    color: var(--muted);
    font-weight: 400;
  }
  .about__title {
    margin: 6px 0 0;
    font-size: 28px;
    font-weight: 400;
    color: var(--navy);
  }
  .about__text {
    margin: 30px 0 0;
    width: 560px;
    font-size: 12.5px;
    line-height: 20px;
    color: var(--body-text);
  }
  .about__photo {
    position: absolute;
    left: 740px;
    top: 74px;
    width: 340px;
    height: 80px;
    background: linear-gradient(90deg, #d9d9d9 0%, #f1f1f1 45%, #e6e2dc 80%, #c9a98c 100%);
    box-shadow: 0 0 18px rgba(232, 120, 100, 0.35);
  }
</style>
</head>
<body>
<div class="page">
  <header class="site-header">
    <svg class="contact-bar" viewBox="0 0 1200 36" aria-hidden="true">
      <polygon points="380,0 1200,0 1200,36 412,36" fill="var(--brand-red)"/>
    </svg>
    <div class="contact-bar__info">
      <span class="contact-bar__item">
        <svg width="10" height="10" viewBox="0 0 24 24" aria-hidden="true"><path fill="#fff" d="M6.6 10.8a15.1 15.1 0 0 0 6.6 6.6l2.2-2.2c.3-.3.7-.4 1-.2 1.1.4 2.3.6 3.6.6.6 0 1 .4 1 1V20c0 .6-.4 1-1 1A17 17 0 0 1 3 4c0-.6.4-1 1-1h3.5c.6 0 1 .4 1 1 0 1.3.2 2.5.6 3.6.1.3 0 .7-.2 1z"/></svg>
        +1 800 555 01 47
      </span>
      <span class="contact-bar__item">
        <svg width="11" height="9" viewBox="0 0 22 16" aria-hidden="true"><rect width="22" height="16" rx="1" fill="#fff"/><path d="M1 1l10 8 10-8" fill="none" stroke="var(--brand-red)" stroke-width="1.6"/></svg>
        info@brantwoodpower.co.nz
      </span>
    </div>

    <a class="brand" href="#">
      <span class="brand__mark"></span>
      <span class="brand__name">Brantwood Power</span>
    </a>

    <nav class="main-nav">
      <a href="#" class="is-active">HOME</a>
      <a href="#">ABOUT US</a>
      <a href="#">OUR SERVICES</a>
      <a href="#">PROJECTS</a>
      <a href="#">BLOG</a>
      <a href="#">CONTACT US</a>
    </nav>
  </header>

  <svg class="hero" viewBox="0 0 1200 432">
    <defs>
      <linearGradient id="plant-room" x1="0" y1="0" x2="0" y2="1">
        <stop offset="0" stop-color="#9a9c9c"/>
        <stop offset="0.55" stop-color="#6f6e6c"/>
        <stop offset="1" stop-color="#a3231f"/>
      </linearGradient>
      <linearGradient id="night-house" x1="0" y1="0" x2="0" y2="1">
        <stop offset="0" stop-color="#0c1a4d"/>
        <stop offset="0.5" stop-color="#23386e"/>
        <stop offset="0.75" stop-color="#7a5230"/>
        <stop offset="1" stop-color="#3f7a2a"/>
      </linearGradient>
      <linearGradient id="stair-hall" x1="0" y1="0" x2="1" y2="1">
        <stop offset="0" stop-color="#6b4a25"/>
        <stop offset="0.5" stop-color="#c9944f"/>
        <stop offset="1" stop-color="#5a3f22"/>
      </linearGradient>
    </defs>
    <g role="img" aria-label="Plant room with red fire pump equipment and overhead ducting">
      <polygon points="0,0 505,0 330,432 0,432" fill="url(#plant-room)"/>
    </g>
    <g role="img" aria-label="Modern house lit up at night with a row of soffit lights">
      <polygon points="522,0 893,0 718,432 347,432" fill="url(#night-house)"/>
    </g>
    <g role="img" aria-label="Interior staircase with warm LED step lighting">
      <polygon points="910,0 1200,0 1200,432 735,432" fill="url(#stair-hall)"/>
    </g>
  </svg>

  <section class="about">
    <h3 class="about__eyebrow">About Us</h3>
    <h2 class="about__title">Who we are ?</h2>
    <p class="about__text">We have many years of foreign experience on projects for affluent clients.<br>We know, how to privde high quality work, While on the job site, We do not perceive</p>
    <div class="about__photo" role="img" aria-label="Portrait of the company founder"></div>
  </section>
</div>
</body>
</html>
```